Harrowgate Estates Business Card for Apartment Buildings

Create business cards for resident managers who run apartment buildings. The audience is the public who are searching for apartment rentals, and current residents who live at the apartment building. Key design element will be incorporating the company logo, however, the logo cannot dominate. The building name and manager name are more important than the logo. Current business card design leaves little room for copy, so we may need to reduce the size on the current card to allow for more space for copy.

Target Market(s)

Adults 18-65 years of age, who are looking for an apartment rental, plus current residents who live at our apartment buildings.

Industry/Entity Type

Property Management

Contact Information for Business Card

A major design element will be use of the company logo. Important property and manager contact information must be part of the design. The size of the logo will need to be reduced to make room for building and manager contact copy.

Font styles to use
Sans Serif

Colors
3176b5
000000
959595
ffffff

Requirements
Must have
• 1) Incorporate the company logo.
• 2) Use the company colors (dark blue, black/grey, over white).
• 3) FEATURE THE BUILDING NAME
• 4) FEATURE THE MANAGER NAME
• 5) The company name is less important than BUILDING and MANAGER
• 6) Manager contact information
• **SEE ATTACHED CREATIVE BRIEF**
Nice to have
• 1) Back of card logo watermark
• 2) Ability to write notes on back of carfd
Should not have
• Avoid letting the company logo dominate the card, the building name and manager are more important than the company logo.

```html
<!DOCTYPE html>
<html lang="en">
<head>
<meta charset="utf-8">
<title>Harrowgate Estates – Resident Manager Business Card</title>
<link href="https://fonts.googleapis.com/css2?family=Mulish:wght@400;500;600;700;800&display=swap" rel="stylesheet">
<style>
  :root {
    --brand-blue: #1469a8;
    --ink-grey: #48484a;
    --rule-grey: #4a4a4c;
    --dot-ink: #3a3a3a;
    --paper: #ffffff;
    --backdrop: #ececec;
  }
  * { margin: 0; padding: 0; box-sizing: border-box; }
  html, body { width: 1200px; height: 1200px; overflow: hidden; }
  body {
    background: var(--backdrop);
    font-family: "Mulish", Arial, sans-serif;
    position: relative;
  }
  .card {
    position: absolute;
    left: 207px;
    width: 786px;
    height: 464px;
    background: var(--paper);
    overflow: hidden;
  }
  .card--front { top: 88px; }
  .card--back { top: 646px; height: 463px; }

  /* Company wordmark */
  .wordmark {
    position: absolute;
    display: flex;
    align-items: center;
    gap: 12px;
    color: var(--brand-blue);
    font-weight: 800;
    white-space: nowrap;
  }
  .wordmark__square { background: var(--brand-blue); flex: none; }
  .card--front .wordmark { right: 30px; top: 42px; font-size: 34px; letter-spacing: 0.5px; }
  .card--front .wordmark__square { width: 30px; height: 30px; }
  .card--back .wordmark { left: 50%; top: 50px; transform: translateX(-50%); font-size: 36px; color: var(--paper); }
  .card--back .wordmark__square { width: 30px; height: 30px; background: var(--paper); }

  .manager-name {
    position: absolute; left: 27px; top: 224px;
    font-size: 32px; font-weight: 700; color: var(--brand-blue); letter-spacing: -0.3px;
  }
  .building-name {
    position: absolute; right: 30px; top: 224px;
    font-size: 30px; font-weight: 700; color: var(--brand-blue); letter-spacing: -0.3px;
  }
  .manager-title {
    position: absolute; left: 27px; top: 264px;
    font-size: 18px; font-weight: 600; color: var(--ink-grey);
  }
  .title-rule {
    position: absolute; left: 199px; right: 29px; top: 275px;
    height: 3px; background: var(--rule-grey);
  }
  .contact-list { position: absolute; left: 27px; top: 300px; list-style: none; }
  .contact-list li {
    display: flex; align-items: center; gap: 14px;
    height: 32px; font-size: 19px; font-weight: 600; color: var(--ink-grey);
  }
  .contact-list li:last-child { font-weight: 500; }
  .contact-icon { width: 24px; height: 24px; flex: none; }
  .address {
    position: absolute; right: 30px; top: 322px; text-align: right;
    font-size: 18px; font-weight: 600; color: var(--ink-grey); line-height: 20px;
  }
  .front-footer { position: absolute; left: 0; bottom: 0; width: 786px; height: 70px; }
  .website {
    position: absolute; right: 28px; bottom: 20px;
    font-size: 17px; font-weight: 700; color: var(--paper); letter-spacing: 0.6px;
  }

  /* Back */
  .back-header { position: absolute; left: 0; top: 0; width: 100%; height: 144px; background: var(--brand-blue); }
  .back-footer { position: absolute; left: 0; bottom: 0; width: 100%; height: 29px; background: var(--brand-blue); }
  .notes-label {
    position: absolute; left: 28px; top: 151px;
    font-size: 23px; font-weight: 600; color: var(--ink-grey);
  }
  .notes-lines { position: absolute; left: 0; top: 0; width: 786px; height: 463px; }
</style>
</head>
<body>

<section class="card card--front" aria-label="Business card front">
  <div class="wordmark"><span class="wordmark__square"></span>HARROWGATE ESTATES</div>

  <h1 class="manager-name">Marisol Delgado</h1>
  <h2 class="building-name">Cedar Court Apartments</h2>
  <p class="manager-title">Resident Manager</p>
  <div class="title-rule"></div>

  <ul class="contact-list">
    <li>
      <svg class="contact-icon" viewBox="0 0 24 24" aria-hidden="true">
        <circle cx="12" cy="12" r="12" fill="var(--brand-blue)"/>
        <path d="M8 6.5c.6-.5 1.3-.4 1.7.2l1 1.6c.3.5.2 1.1-.2 1.4l-.8.6c.6 1.3 1.7 2.5 3 3.1l.6-.8c.4-.4 1-.5 1.4-.2l1.6 1c.6.4.7 1.1.2 1.7l-.9 1c-.6.6-1.6.8-2.4.4-2.8-1.3-5-3.5-6.3-6.3-.4-.8-.2-1.8.4-2.4z" fill="#fff"/>
      </svg>
      555-210-4837
    </li>
    <li>
      <svg class="contact-icon" viewBox="0 0 24 24" aria-hidden="true">
        <circle cx="12" cy="12" r="12" fill="var(--brand-blue)"/>
        <rect x="8.5" y="5.5" width="7" height="13" rx="1.5" fill="none" stroke="#fff" stroke-width="1.8"/>
        <circle cx="12" cy="16" r="0.9" fill="#fff"/>
      </svg>
      555-648-3190
    </li>
    <li>
      <svg class="contact-icon" viewBox="0 0 24 24" aria-hidden="true">
        <circle cx="12" cy="12" r="12" fill="var(--brand-blue)"/>
        <rect x="8.5" y="5.5" width="7" height="4" fill="none" stroke="#fff" stroke-width="1.5"/>
        <rect x="6" y="9.5" width="12" height="6" rx="1" fill="#fff"/>
        <rect x="8.5" y="13.5" width="7" height="5" fill="#fff" stroke="var(--brand-blue)" stroke-width="1"/>
      </svg>
      555-372-9015
    </li>
    <li>
      <svg class="contact-icon" viewBox="0 0 24 24" aria-hidden="true">
        <circle cx="12" cy="12" r="12" fill="var(--brand-blue)"/>
        <rect x="6" y="8" width="12" height="9" rx="1.5" fill="#fff"/>
        <path d="M6.5 9l5.5 4 5.5-4" fill="none" stroke="var(--brand-blue)" stroke-width="1.5"/>
      </svg>
      marisol@harrowgateest.com
    </li>
  </ul>

  <p class="address">2840 Linden Avenue<br>Fairview, CA 92177</p>

  <svg class="front-footer" viewBox="0 394 786 70" aria-hidden="true">
    <path d="M0 434 H452 C462 434 466 432 470 429 L474 426 V444 H0 Z" fill="var(--rule-grey)"/>
    <path d="M0 446 H452 C478 446 484 406 514 406 H786 V464 H0 Z" fill="var(--brand-blue)"/>
  </svg>
  <p class="website">www.harrowgateest.com</p>
</section>

<section class="card card--back" aria-label="Business card back">
  <div class="back-header"></div>
  <div class="wordmark"><span class="wordmark__square"></span>HARROWGATE ESTATES</div>

  <svg class="notes-lines" viewBox="0 0 786 463" aria-hidden="true">
    <g stroke="var(--dot-ink)" stroke-width="2.4" stroke-dasharray="2.4 2.2">
      <line x1="170" y1="174" x2="754" y2="174"/>
      <line x1="28" y1="204" x2="754" y2="204"/>
      <line x1="28" y1="235" x2="754" y2="235"/>
      <line x1="28" y1="266" x2="754" y2="266"/>
      <line x1="28" y1="297" x2="754" y2="297"/>
      <line x1="28" y1="328" x2="754" y2="328"/>
      <line x1="28" y1="358" x2="754" y2="358"/>
      <line x1="28" y1="389" x2="754" y2="389"/>
      <line x1="28" y1="420" x2="754" y2="420"/>
    </g>
  </svg>
  <p class="notes-label">Write Notes :</p>

  <div class="back-footer"></div>
</section>

</body>
</html>
```